Business Card Design

We need a business card designed for a new company based in Melbourne called Korvum solutions. Korvum solutions provides management consulting specialising in the health and social services sector.

Korvum solutions offer a unique set of specialist skills │dealing with all levels of government │ unique communication skills│intimate knowledge of the health sector │solutions tailored to unique circumstances.

Korvum solutions takes on a select number of clients at any one time, this ensures that your organisation receives the attention required. On larger projects, Korvum solutions join up with other consultants to bring specialist skills to a project.
Updates

This is the first time I have used Pixel Bazaar and thank you all for responding. The variation is amazing and makes it hard to decide. I have to ask some of my friends to give me their views. The response is fantastic. The one I pick will basically be the most visually appealing

Industry/Entity Type

Management Consulting

Contact Information for Business Card

Marcus Pellow, Principal, Korvum solutions, 14 Wexcombe Ave, Dunlarry VIC 3999, 0400 137 284, marcusp@korvumsolutions.example, www.korvumsolutions.example

```html
<!DOCTYPE html>
<html lang="en">
<head>
<meta charset="utf-8">
<title>Korvum solutions – Business Card</title>
<link href="https://fonts.googleapis.com/css2?family=Questrial&display=swap" rel="stylesheet">
<style>
  :root {
    --brand-red: #bf0010;
    --pattern-red: #d0345a;
    --ink: #111111;
    --paper: #f2f2f2;
    --paper-light: #ffffff;
    --pattern-grey: #e9e9e9;
  }
  html, body {
    margin: 0;
    padding: 0;
    width: 1200px;
    height: 741px;
    overflow: hidden;
    background: #ffffff;
  }
  .card {
    position: relative;
    width: 1200px;
    height: 741px;
    overflow: hidden;
    font-family: "Questrial", "Century Gothic", sans-serif;
    background: var(--paper);
  }
  .card__band {
    position: absolute;
    left: 0; top: 0;
    width: 1200px;
    height: 292px;
    background: var(--brand-red);
  }
  .card__texture-top {
    position: absolute;
    left: 771px; top: 38px;
    width: 286px; height: 238px;
    background: linear-gradient(135deg, rgba(208,52,90,0.55), rgba(208,52,90,0.35));
  }
  .card__texture-bottom {
    position: absolute;
    left: 0; top: 540px;
    width: 286px; height: 201px;
    background: linear-gradient(90deg, var(--pattern-grey), rgba(233,233,233,0.3));
  }
  .card__swoosh {
    position: absolute;
    left: 0; top: 292px;
    width: 1200px; height: 449px;
  }
  .brand-name {
    position: absolute;
    left: 84px; top: 118px;
    margin: 0;
    color: #ffffff;
    font-size: 68px;
    font-weight: 400;
    letter-spacing: 1px;
    line-height: 1;
  }
  .person {
    position: absolute;
    right: 95px; top: 322px;
    text-align: right;
  }
  .person__name {
    margin: 0;
    font-size: 53px;
    font-weight: 400;
    color: var(--ink);
    line-height: 1;
  }
  .person__role {
    margin: 4px 0 0;
    font-size: 34px;
    color: var(--brand-red);
    line-height: 1.1;
  }
  .contact {
    position: absolute;
    right: 72px; top: 526px;
    margin: 0; padding: 0;
    list-style: none;
    text-align: right;
  }
  .contact__item {
    display: flex;
    justify-content: flex-end;
    align-items: center;
    gap: 10px;
    height: 36px;
    font-size: 31px;
    color: var(--ink);
    line-height: 1;
  }
  .contact__item--web { color: var(--brand-red); }
  .contact__icon {
    width: 24px; height: 24px;
    flex: none;
    fill: var(--brand-red);
  }
</style>
</head>
<body>
<div class="card">
  <div class="card__band"></div>
  <div class="card__texture-top" role="img" aria-label="Grid of small plus-sign pattern on the red band"></div>

  <svg class="card__swoosh" viewBox="0 0 1200 449" aria-hidden="true">
    <defs>
      <linearGradient id="paperShade" x1="0" y1="0" x2="0" y2="1">
        <stop offset="0" stop-color="#ececec"/>
        <stop offset="0.4" stop-color="#f7f7f7"/>
        <stop offset="1" stop-color="#f0f0f0"/>
      </linearGradient>
    </defs>
    <rect width="1200" height="449" fill="url(#paperShade)"/>
    <path d="M0 150 C300 80 700 60 1200 120 L1200 170 C750 110 350 120 0 200 Z" fill="#ffffff" opacity="0.9"/>
    <path d="M0 170 C400 110 800 110 1200 180 L1200 190 C800 125 400 130 0 185 Z" fill="#e4e4e4" opacity="0.8"/>
    <path d="M0 260 C450 200 850 220 1200 300 L1200 449 L0 449 Z" fill="#ffffff" opacity="0.5"/>
  </svg>

  <div class="card__texture-bottom" role="img" aria-label="Faint grid of small plus-sign pattern in the lower corner"></div>

  <h1 class="brand-name">Korvum solutions</h1>

  <div class="person">
    <p class="person__name">Marcus Pellow</p>
    <p class="person__role">Principal</p>
  </div>

  <ul class="contact">
    <li class="contact__item">0400 137 284
      <svg class="contact__icon" viewBox="0 0 24 24" aria-hidden="true"><path d="M2 9c0-3 5-5 10-5s10 2 10 5v2h-5V9c-1-1-3-1-5-1s-4 0-5 1v2H2z M6 12h12l2 7H4z"/><circle cx="12" cy="15.5" r="2" fill="#fff"/></svg>
    </li>
    <li class="contact__item">Wexcombe Ave, Dunlarry VIC 3999
      <svg class="contact__icon" viewBox="0 0 24 24" aria-hidden="true"><rect x="10.5" y="2" width="3" height="21"/><path d="M3 5h17l3 3-3 3H3z M21 13H4l-3 3 3 3h17z"/></svg>
    </li>
    <li class="contact__item">marcusp@korvumsolutions.example
      <svg class="contact__icon" viewBox="0 0 24 24" aria-hidden="true"><path d="M2 5h20v14H2z"/><path d="M2 5l10 8 10-8" fill="none" stroke="#fff" stroke-width="2"/></svg>
    </li>
    <li class="contact__item contact__item--web">www.korvumsolutions.example
      <svg class="contact__icon" viewBox="0 0 24 24" aria-hidden="true"><circle cx="12" cy="12" r="11"/><path d="M6 6c2 1 3 3 2 5s1 3 2 5-1 4-1 5M15 4c-1 2 1 3 3 3s2 3 0 4-1 4 1 5" fill="none" stroke="#fff" stroke-width="2"/></svg>
    </li>
  </ul>
</div>
</body>
</html>
```